Web design for Modeling agency

We are looking for re-designing our modeling agency website.
Current website: lunafaces.com our competitor: KTRfaces.com
http://brisaface.fr/
https://www.corvelmanagement.com/models/
https://www.hedwig-faces.de
https://www.rustmanagement.co.uk
https://www.quorbfaces.com
https://www.harborlightfaces.com

Target Market(s)

modeling agency

Industry/Entity Type

modeling agency

Number of Pages Required

5+ page

Font styles to use
Other font styles liked:
• base on logo guidline

Requirements
Nice to have
• current website: lunafaces.com our competitor: KTRfaces.com

```html
<!DOCTYPE html>
<html lang="en">
<head>
<meta charset="utf-8">
<title>Luna Face Management</title>
<link rel="stylesheet" href="https://fonts.googleapis.com/css2?family=Questrial&family=Crimson+Text&display=swap">
<style>
:root{
  --board:#3b3b3b;
  --tan:#c4a088;
  --ink:#2b2b2b;
  --muted:#c9c9c9;
  --light:#f4f4f4;
  --white:#ffffff;
  --footer:#1b1b1b;
  --hero-warm:#6a4a36;
  --hero-blue:#2e4256;
  --hero-dark:#1c1c1e;
}
*{box-sizing:border-box;margin:0;padding:0}
html,body{width:1200px;height:3932px;overflow:hidden}
body{background:var(--board);font-family:"Questrial",sans-serif;color:var(--ink);position:relative}
.panel{position:absolute;left:41px;width:1116px;overflow:hidden}
.abs{position:absolute}
.center{left:0;right:0;text-align:center}

/* splash */
.splash{top:40px;height:557px}
.photo-split{position:absolute;inset:0;background:
  radial-gradient(ellipse 180px 230px at 390px 250px,rgba(214,160,122,.55),transparent 70%),
  radial-gradient(ellipse 120px 160px at 800px 130px,rgba(190,140,110,.35),transparent 70%),
  linear-gradient(100deg,var(--hero-warm) 0%,#4d3a2e 18%,var(--hero-blue) 36%,#3d3a3a 57%,var(--hero-dark) 60%,#0f0f10 100%)}
.splash .shade{position:absolute;inset:0;background:rgba(0,0,0,.22)}
.wordmark{color:var(--white);font-weight:400;letter-spacing:2px;text-align:center;line-height:1}
.splash .wordmark-main{left:180px;width:400px;top:180px;font-size:124px}
.splash .wordmark-sub{left:180px;width:400px;top:334px;font-size:48px;letter-spacing:1px}
.divider{left:655px;top:87px;width:2px;height:382px;background:var(--white)}
.city{left:704px;width:183px;height:47px;border:2px solid var(--white);border-radius:6px;color:var(--white);font-size:22px;display:flex;align-items:center;justify-content:center;letter-spacing:.5px}
.city.active{background:var(--tan);border-color:var(--tan)}

/* site */
.site{top:643px;height:3249px;background:var(--white)}
.hero{top:0;left:0;width:1116px;height:559px}
.hero .shade{position:absolute;inset:0;background:rgba(0,0,0,.42)}
.nav-logo{left:104px;top:14px;width:128px;color:var(--white);text-align:center;line-height:1}
.nav-logo .main{font-size:40px;letter-spacing:1px}
.nav-logo .sub{font-size:15px;margin-top:4px}
.nav a{position:absolute;top:38px;color:var(--white);font-size:12px;text-decoration:none;letter-spacing:.3px}
.search{left:996px;top:36px}
.hero h1{top:170px;font-size:52px;font-weight:400;color:var(--white);letter-spacing:1px}
.hero p{left:183px;width:750px;top:256px;font-family:"Crimson Text",serif;font-size:14.5px;line-height:26px;color:var(--white);text-align:center}
.btn{display:flex;align-items:center;justify-content:center;border-radius:4px;font-size:18px;letter-spacing:.5px}
.btn-tan{left:479px;top:350px;width:159px;height:48px;background:var(--tan);color:var(--white)}
.hero-label{top:511px;color:#cfcfcf;font-size:12px}

.section-title{font-size:35px;font-weight:400;letter-spacing:1px;color:var(--ink)}
.rule{left:529px;width:58px;height:6px;background:var(--tan)}
.rule.white{background:var(--white)}

.explore{top:559px;left:0;width:1116px;height:559px}
.tabs{top:147px;font-size:14px;color:var(--muted);letter-spacing:.5px}
.tabs .on{color:var(--tan)}
.tabs span{margin:0 10px}
.model-card{width:205px;height:258px;border-radius:10px;z-index:1}
.model-name{width:205px;text-align:center;font-size:17px;top:470px}
.arrow{width:36px;height:36px;border-radius:50%;background:var(--tan);top:310px;display:flex;align-items:center;justify-content:center;z-index:3;box-shadow:0 0 0 2px rgba(255,255,255,.6)}

.about{top:1118px;left:0;width:1116px;height:433px;background:var(--tan)}
.about .ghost{left:0;right:0;top:20px;text-align:center;font-size:330px;color:rgba(255,255,255,.12);letter-spacing:10px;line-height:1}
.about .section-title{color:var(--white)}
.about p{left:180px;width:757px;top:140px;font-family:"Crimson Text",serif;font-size:13.5px;line-height:26px;color:var(--white);text-align:center}
.btn-white{left:479px;top:310px;width:159px;height:50px;background:var(--white);color:var(--tan)}

.mother{top:1551px;left:0;width:1116px;height:608px;background:var(--light)}
.agency-card{top:155px;width:283px;height:336px;border-radius:8px}
.agency-label{top:469px;width:252px;height:46px;background:var(--tan);border-radius:6px;color:var(--white);font-size:22px;display:flex;align-items:center;justify-content:center;letter-spacing:1px}

.insta{top:2159px;left:0;width:1116px;height:669px}
.handle{top:148px;font-size:17px;color:#444;display:flex;justify-content:center;align-items:center;gap:8px}
.handle i{width:14px;height:14px;border:2px solid #444;border-radius:4px;display:inline-block}
.tile{width:211px;height:190px}

.footer{top:2828px;left:0;width:1116px;height:421px;background:var(--footer)}
.footer .main{top:52px;font-size:80px;line-height:1}
.footer .sub{top:143px;font-size:30px;line-height:1}
.fnav{top:196px;font-size:12px;color:var(--white);letter-spacing:.3px}
.fnav span{margin:0 14px}
.email{left:301px;top:236px;width:516px;height:49px;background:var(--white);border-radius:25px}
.email span{position:absolute;left:28px;top:15px;font-family:"Crimson Text",serif;font-size:14px;color:#555}
.send{position:absolute;right:6px;top:6px;width:37px;height:37px;border-radius:50%;background:var(--tan)}
.copy{top:304px;font-size:13.5px;color:var(--white)}
.social{top:339px;width:28px;height:28px;border-radius:50%;background:var(--tan)}
</style>
</head>
<body>

<section class="panel splash" aria-label="City selection page">
  <div class="photo-split" role="img" aria-label="Split portrait photo: female model in blue knit sweater on the left, male model in black cap and hoodie on the right"></div>
  <div class="shade"></div>
  <div class="abs wordmark wordmark-main">LUNA</div>
  <div class="abs wordmark wordmark-sub">MODEL MGMT</div>
  <div class="abs divider"></div>
  <div class="abs city" style="top:108px">LONDON</div>
  <div class="abs city" style="top:168px">PARIS</div>
  <div class="abs city active" style="top:227px">ISTANBUL</div>
  <div class="abs city" style="top:287px">MILAN</div>
  <div class="abs city" style="top:346px">ATHENS</div>
  <div class="abs city" style="top:406px">DUBAI</div>
</section>

<main class="panel site">
  <header class="abs hero">
    <div class="photo-split" role="img" aria-label="Hero photo: female model on the left, male model on the right"></div>
    <div class="shade"></div>
    <div class="abs nav-logo"><div class="main">LUNA</div><div class="sub">MODEL MGMT</div></div>
    <nav class="nav">
      <a style="left:256px">WOMEN</a>
      <a style="left:339px">MEN</a>
      <a style="left:398px">IN TOWN</a>
      <a style="left:485px">LUNA MOTHER AGENCY</a>
      <a style="left:670px">BE A MODEL</a>
      <a style="left:780px">ABOUT</a>
      <a style="left:858px">CONTACT</a>
      <a style="left:944px">ENG ▾</a>
    </nav>
    <svg class="abs search" width="16" height="16" viewBox="0 0 16 16"><circle cx="6.5" cy="6.5" r="4.5" fill="none" stroke="#fff" stroke-width="2"/><line x1="10" y1="10" x2="14" y2="14" stroke="#fff" stroke-width="2.4" stroke-linecap="round"/></svg>
    <h1 class="abs center">LUNA MODEL MANAGEMENT</h1>
    <p class="abs">Luna Face Management ensures to nurture our models for them to reach the limelight and to establish good working avenue where each individual can reach its full potential. The company will strive to be the best management for career development in the industry.</p>
    <div class="abs btn btn-tan">GET STARTED</div>
    <div class="abs hero-label" style="left:181px">WOMEN</div>
    <div class="abs hero-label" style="left:855px">MEN</div>
  </header>

  <section class="abs explore">
    <h2 class="abs center section-title" style="top:68px">EXPLORE OUR WORLD</h2>
    <div class="abs rule" style="top:118px"></div>
    <div class="abs center tabs"><span>ALL</span>|<span class="on">WOMEN</span>|<span>MEN</span>|<span>IN TOWN</span></div>
    <div class="abs model-card" style="left:124px;top:199px;background:radial-gradient(ellipse 60px 80px at 110px 80px,rgba(190,150,120,.5),transparent 70%),linear-gradient(165deg,#cfc6bb,#e6d8c2 55%,#b59c7f)" role="img" aria-label="Portrait of model Mira in a cream jacket"></div>
    <div class="abs model-card" style="left:345px;top:199px;background:radial-gradient(ellipse 70px 90px at 110px 95px,rgba(220,220,220,.6),transparent 70%),linear-gradient(165deg,#7a7a7a,#3a3a3a 60%,#1e1e1e)" role="img" aria-label="Black and white portrait of model Elin"></div>
    <div class="abs model-card" style="left:567px;top:199px;background:radial-gradient(ellipse 70px 90px at 100px 120px,rgba(222,170,140,.75),transparent 72%),linear-gradient(165deg,#a9b7bf,#c7a890 70%,#b38a6c)" role="img" aria-label="Portrait of model Tova in a blue cap"></div>
    <div class="abs model-card" style="left:788px;top:199px;background:radial-gradient(ellipse 60px 110px at 110px 170px,rgba(20,20,20,.8),transparent 70%),linear-gradient(165deg,#ecebe8,#d9d4ce 60%,#a9a39c)" role="img" aria-label="Portrait of model Rhea seated in black dress"></div>
    <div class="abs arrow" style="left:103px"><svg width="10" height="10" viewBox="0 0 10 10"><path d="M6.5 2 3.5 5l3 3" fill="none" stroke="#fff" stroke-width="1.6"/></svg></div>
    <div class="abs arrow" style="left:976px"><svg width="10" height="10" viewBox="0 0 10 10"><path d="M3.5 2l3 3-3 3" fill="none" stroke="#fff" stroke-width="1.6"/></svg></div>
    <div class="abs model-name" style="left:124px">MIRA</div>
    <div class="abs model-name" style="left:345px">ELIN</div>
    <div class="abs model-name" style="left:567px">TOVA</div>
    <div class="abs model-name" style="left:788px">RHEA</div>
  </section>

  <section class="abs about">
    <div class="abs ghost" aria-hidden="true">LUNA</div>
    <h2 class="abs center section-title" style="top:66px">ABOUT LUNAFACES</h2>
    <div class="abs rule white" style="top:116px"></div>
    <p class="abs">Luna Face Management strives on being one of best high fashion model agency in Turkey with the help of several top models in the modeling industry. Operating in Turkey, Luna Face Management has also made its name in London where the company has expanded its office to. Working with models who you see in billboards, magazines, printed and online advertisements and many more. Luna Face Management is established by inspiration, therefore, it will also inspire beautiful models and work with them as they further develop their careers. The company guarantees a safe working space that focuses on helping models reach their full potential and achieve their dreams with the help of our good and trusted management service.</p>
    <div class="abs btn btn-white">LEARN MORE</div>
  </section>

  <section class="abs mother">
    <h2 class="abs center section-title" style="top:66px">LUNA MOTHER AGENCY</h2>
    <div class="abs rule" style="top:116px"></div>
    <div class="abs agency-card" style="left:114px;background:radial-gradient(ellipse 70px 150px at 140px 210px,rgba(205,150,150,.75),transparent 72%),linear-gradient(170deg,#f2f2f2,#e4e1df)" role="img" aria-label="Model Ines in a pink fringed dress in a white room"></div>
    <div class="abs agency-card" style="left:418px;background:radial-gradient(ellipse 90px 130px at 140px 230px,rgba(226,220,160,.85),transparent 72%),linear-gradient(170deg,#cdb9a4,#d9c6b0)" role="img" aria-label="Model Lia Bo in a pale checked blazer"></div>
    <div class="abs agency-card" style="left:722px;background:radial-gradient(ellipse 90px 100px at 140px 230px,rgba(255,255,255,.9),transparent 72%),radial-gradient(ellipse 60px 90px at 140px 90px,rgba(214,170,110,.75),transparent 72%),linear-gradient(170deg,#b7d0dd,#7f9a78 60%,#d7dde2)" role="img" aria-label="Model Nora K in a white tee and sunglasses outdoors"></div>
    <div class="abs agency-label" style="left:130px">INES</div>
    <div class="abs agency-label" style="left:434px">LIA BO</div>
    <div class="abs agency-label" style="left:738px">NORA K</div>
  </section>

  <section class="abs insta">
    <h2 class="abs center section-title" style="top:70px">FOLLOW US TO INSTAGRAM</h2>
    <div class="abs rule" style="top:120px"></div>
    <div class="abs center handle"><i aria-hidden="true"></i>@lunafaces</div>
    <div class="abs tile" style="left:122px;top:189px;background:radial-gradient(ellipse 70px 90px at 105px 90px,rgba(200,200,200,.55),transparent 70%),linear-gradient(150deg,#6a6a6a,#222)" role="img" aria-label="Black and white male portrait"></div>
    <div class="abs tile" style="left:342px;top:189px;background:radial-gradient(ellipse 60px 80px at 120px 80px,rgba(225,195,180,.7),transparent 70%),linear-gradient(150deg,#2f6f8f,#5e9ab6)" role="img" aria-label="Female model by blue water"></div>
    <div class="abs tile" style="left:563px;top:189px;background:radial-gradient(ellipse 80px 80px at 130px 80px,rgba(200,130,90,.85),transparent 70%),linear-gradient(150deg,#3e8eb5,#7fb7d1)" role="img" aria-label="Magazine cover with male model"></div>
    <div class="abs tile" style="left:785px;top:189px;background:radial-gradient(ellipse 60px 80px at 105px 85px,rgba(176,125,95,.7),transparent 70%),linear-gradient(150deg,#e3ddd6,#cfc5ba)" role="img" aria-label="Female model in white blazer"></div>
    <div class="abs tile" style="left:122px;top:388px;background:radial-gradient(ellipse 60px 90px at 110px 110px,rgba(20,20,20,.85),transparent 70%),linear-gradient(150deg,#9bb6cf,#c9d6e2)" role="img" aria-label="Fashion magazine cover with model in black coat"></div>
    <div class="abs tile" style="left:342px;top:388px;background:radial-gradient(ellipse 80px 90px at 100px 100px,rgba(196,150,115,.9),transparent 72%),linear-gradient(150deg,#8a6a52,#3c2a20)" role="img" aria-label="Male model in sunglasses"></div>
    <div class="abs tile" style="left:563px;top:388px;background:radial-gradient(ellipse 50px 20px at 110px 45px,rgba(230,80,170,.9),transparent 80%),linear-gradient(150deg,#6a6a6a,#2a2a2a)" role="img" aria-label="Black and white magazine cover with pink highlight"></div>
    <div class="abs tile" style="left:785px;top:388px;background:radial-gradient(ellipse 70px 90px at 110px 130px,rgba(176,130,90,.9),transparent 72%),linear-gradient(150deg,#4d8fbf,#8ab7d8)" role="img" aria-label="Male model in tan suit against blue sky"></div>
  </section>

  <footer class="abs footer">
    <div class="abs center wordmark main">LUNA</div>
    <div class="abs center wordmark sub">MODEL MGMT</div>
    <div class="abs center fnav"><span>WOMEN</span><span>MEN</span><span>IN TOWN</span><span>LUNA MOTHER AGENCY</span><span>BE A MODEL</span><span>ABOUT</span><span>CONTACT</span></div>
    <div class="abs email"><span>Enter The Email</span>
      <div class="send"><svg width="37" height="37" viewBox="0 0 37 37"><path d="M11 19l15-7-6 15-2-6z" fill="none" stroke="#fff" stroke-width="1.6" stroke-linejoin="round"/></svg></div>
    </div>
    <div class="abs center copy">© Copyrights 2021 Luna Face Agency &nbsp;| &nbsp; All Rights Reserved</div>
    <div class="abs social" style="left:484px" aria-label="Social link"></div>
    <div class="abs social" style="left:525px" aria-label="Social link"></div>
    <div class="abs social" style="left:566px" aria-label="Social link"></div>
    <div class="abs social" style="left:606px" aria-label="Social link"></div>
  </footer>
</main>

</body>
</html>
```